Business Card Design for Event Planning Company

Create a business card for event planning company using our new logo. After I pick the design, I will need files made for 6 employees. Our company provides event design & logistics services as well as venue management. The font should be sans serif and complementary to the logo. I will need to know the name of the font selected for the final design. The phone numbers listed should be separated by "." not "-"

Address for the card
PO Box 318, Washington, DC 20019

Card One
Lorna Pettibone
lpettibone@galavoyant.com
202.481.7730

Card Two
Miriam Okonkwo
mokonkwo@galavoyant.com
202.556.2047

Card Three
Tessa Varnholt
tvarnholt@galavoyant.com
978.620.4471

Card Four
Robin Fess
rfess@galavoyant.com
202.718.3362

Card Five
Ada-Rose Pelletan-Uzor
adarose@galavoyant.com
202.839.1205

Card Six
Beatrix Holloway
Beatrix@galavoyant.com
202.492.6618

Target Market(s)

Corporate/Non-Profit

Industry/Entity Type

Event Planning

Contact Information for Business Card

Address for the card

Card One
Lorna Pettibone
lpettibone@galavoyant.com
202.481.7730

Card Two
Miriam Okonkwo
202.556.2047

Card Three
Tessa Varnholt
978.620.4471

Card Four
Robin Fess
rfess@galavoyant.com
202.718.3362

Card Five
Ada-Rose Pelletan-Uzor
202.839.1205

Card Six
Beatrix Holloway
202.492.6618

Font styles to use
Sans Serif

Colors

Designer to choose colors to be used in the design.

Requirements
Must have
• Two-sided with logo
Should not have
• Extra colors or be too busy

```html
<!DOCTYPE html>
<html lang="en">
<head>
<meta charset="utf-8">
<title>Galavoyant Business Card</title>
<link rel="stylesheet" href="https://fonts.googleapis.com/css2?family=Questrial&display=swap">
<style>
  :root {
    --page-bg: #e4e4e4;
    --card-dark: #2f2f2f;
    --card-light: #f6f6f6;
    --teal: #5ea3a7;
    --ink-light: #e6e6e6;
    --ink-dark: #2c2c2c;
    --ink-soft: #3a3a3a;
  }
  * { margin: 0; padding: 0; box-sizing: border-box; }
  html, body {
    width: 1200px;
    height: 576px;
    overflow: hidden;
    background: var(--page-bg);
    font-family: "Questrial", "Century Gothic", sans-serif;
  }
  .canvas { position: relative; width: 1200px; height: 576px; }
  .card {
    position: absolute;
    top: 138px;
    border-radius: 13px;
    overflow: hidden;
  }
  .card-front {
    left: 82px;
    width: 485px;
    height: 294px;
    background: var(--card-dark);
  }
  .card-back {
    left: 602px;
    width: 482px;
    height: 291px;
    background: var(--card-light);
  }
  .brand-mark {
    position: absolute;
    width: 34px;
    height: 34px;
    border-radius: 50%;
    background: var(--teal);
  }
  .card-front .brand-mark { left: 225px; top: 88px; }
  .card-back .brand-mark { right: 76px; top: 37px; }
  .brand-name {
    position: absolute;
    letter-spacing: 0.5px;
    line-height: 1;
    white-space: nowrap;
    color: var(--teal);
  }
  .card-front .brand-name {
    left: 0; right: 0;
    top: 140px;
    text-align: center;
    font-size: 42px;
  }
  .card-back .brand-name {
    right: 22px;
    top: 85px;
    font-size: 30px;
  }
  .website {
    position: absolute;
    left: 0; right: 0;
    top: 257px;
    display: flex;
    align-items: center;
    justify-content: center;
    gap: 12px;
    font-size: 12.5px;
    color: var(--ink-light);
  }
  .website .rule {
    width: 58px;
    height: 1px;
    background: var(--teal);
  }
  .website .domain { color: var(--teal); }
  .person-name {
    position: absolute;
    left: 20px;
    top: 181px;
    font-size: 21px;
    color: var(--teal);
  }
  .contact-list {
    position: absolute;
    left: 21px;
    top: 215px;
    list-style: none;
    font-size: 13px;
    color: var(--ink-dark);
  }
  .contact-list li {
    display: flex;
    align-items: center;
    gap: 7px;
    height: 17px;
  }
  .contact-list .address { margin-top: 4px; }
  .contact-icon { width: 11px; height: 11px; fill: var(--teal); }
</style>
</head>
<body>
<div class="canvas">
  <section class="card card-front" aria-label="Card front">
    <span class="brand-mark" aria-hidden="true"></span>
    <div class="brand-name">galavoyant</div>
    <div class="website">
      <span class="rule"></span>
      <span>www.<span class="domain">galavoyant</span>.com</span>
      <span class="rule"></span>
    </div>
  </section>

  <section class="card card-back" aria-label="Card back">
    <span class="brand-mark" aria-hidden="true"></span>
    <div class="brand-name">galavoyant</div>
    <h1 class="person-name" style="font-weight:400">Beatrix Holloway</h1>
    <ul class="contact-list">
      <li>
        <svg class="contact-icon" viewBox="0 0 12 12" aria-hidden="true">
          <path d="M1 4c0-1.5 2.2-2.5 5-2.5s5 1 5 2.5v1H8.5V3.8h-5V5H1z"/>
          <rect x="2.5" y="6" width="7" height="5" rx="1"/>
        </svg>
        <span>202.492.6618</span>
      </li>
      <li>
        <svg class="contact-icon" viewBox="0 0 12 12" aria-hidden="true">
          <path d="M0.5 2.5h11v7h-11z M0.5 2.5l5.5 4 5.5-4" fill="none" stroke="#5ea3a7" stroke-width="1.3"/>
        </svg>
        <span>Beatrix@galavoyant.com</span>
      </li>
      <li class="address"><span>PO Box 318, Washington, DC 20019</span></li>
    </ul>
  </section>
</div>
</body>
</html>
```